Business Card Design

We offer full auto repair and auto customization from custom wheels to lift kits and drop kits we do it all. I want something that grabs your attention from the start but nothing flashy i am more of a clean crisp modern kinda of guy. I plan on using the design on my business cards and my main business sign .
Updates
I have up loaded an image of my currant business card designed by me , I would like to improve on it
Target Market(s)
20-35 male and female
Industry/Entity Type
Business
Contact Information for Business Card
Corvello Wheel Works
48362 1/2 Parkfield rd
Houston TX, 77070
Manager: Dorian Walsh
P:555-214-7730
F:555-214-7781
Email:Dorian@corvellowheelandgarage.example
website:Corvellowheelandgarage.example
Look and feel

```html
<!DOCTYPE html>
<html lang="en">
<head>
<meta charset="utf-8">
<title>Corvello Wheel Works – Business Card</title>
<link href="https://fonts.googleapis.com/css2?family=Josefin+Sans:wght@300;400;600;700&display=swap" rel="stylesheet">
<style>
  :root {
    --backdrop: #5ccbbb;
    --card-white: #f4f4f2;
    --ink: #1d1d1f;
    --band-black: #262628;
    --accent-red: #e0161e;
    --tab-grey: #d9d9d9;
    --muted: #6d6d6d;
    --light-text: #f2f2f2;
  }
  * { margin: 0; padding: 0; box-sizing: border-box; }
  html, body { width: 1200px; height: 882px; overflow: hidden; }
  body {
    background: var(--backdrop);
    font-family: "Josefin Sans", "Helvetica Neue", Arial, sans-serif;
    color: var(--ink);
    position: relative;
  }
  .card {
    position: absolute;
    top: 291px;
    width: 525px;
    height: 300px;
    overflow: hidden;
    box-shadow: 0 10px 24px rgba(0,0,0,0.18);
  }
  .card-front { left: 50px; background: var(--card-white); }
  .card-back { left: 625px; background: var(--band-black); }
  .card-shapes { position: absolute; inset: 0; width: 100%; height: 100%; }

  /* Front */
  .name-tab {
    position: absolute; top: 34px; right: 0;
    width: 230px; height: 54px;
    background: var(--tab-grey);
    padding: 11px 0 0 22px;
  }
  .person-name { font-size: 19px; letter-spacing: 1px; text-transform: uppercase; font-weight: 300; }
  .person-name strong { font-weight: 600; }
  .person-role { font-size: 10px; letter-spacing: 2px; color: var(--muted); text-transform: uppercase; margin-top: 4px; }

  .front-brand { position: absolute; left: 36px; top: 100px; }
  .brand-name {
    font-size: 44px; font-weight: 600; letter-spacing: 1px;
    text-transform: uppercase; line-height: 1;
  }
  .brand-tagline {
    font-size: 17px; font-weight: 400; letter-spacing: 1.5px;
    text-transform: uppercase; color: var(--accent-red); margin-top: 6px;
  }
  .front-address {
    position: absolute; left: 36px; top: 180px;
    font-size: 11px; letter-spacing: 1px; color: var(--muted);
  }

  .contact-band {
    position: absolute; left: 0; top: 222px; width: 100%; height: 78px;
    display: grid; grid-template-columns: 170px 1fr;
    align-content: center;
    padding: 0 24px 0 36px; row-gap: 12px;
    color: var(--light-text); font-size: 10.5px; letter-spacing: 0.6px;
  }
  .contact-item { display: flex; align-items: center; gap: 7px; white-space: nowrap; line-height: 1; }
  .contact-item svg { width: 11px; height: 11px; flex: none; fill: var(--light-text); }

  /* Back */
  .back-brand { position: absolute; left: 36px; top: 88px; color: var(--light-text); }
  .back-brand .brand-name { font-size: 40px; }
  .back-brand .brand-tagline { color: var(--light-text); font-size: 15px; font-weight: 300; }

  .service-list {
    position: absolute; right: 26px; top: 26px;
    list-style: none; text-align: right;
    color: var(--light-text); font-size: 10.5px; letter-spacing: 1.2px;
    text-transform: uppercase; line-height: 1.55;
  }
  .range-band {
    position: absolute; left: 0; top: 196px; width: 100%; height: 104px;
    padding: 16px 22px 0 106px; color: var(--light-text);
    text-transform: uppercase;
  }
  .range-title { font-size: 11px; letter-spacing: 1.5px; font-weight: 600; }
  .range-list { font-size: 9px; letter-spacing: 0.6px; line-height: 1.7; margin-top: 6px; white-space: nowrap; }
</style>
</head>
<body>

<section class="card card-front" aria-label="Business card front">
  <svg class="card-shapes" viewBox="0 0 525 300" preserveAspectRatio="none" aria-hidden="true">
    <polygon points="0,222 525,222 525,300 0,300" fill="var(--band-black)"/>
    <polygon points="380,222 525,190 525,222" fill="var(--accent-red)"/>
    <line x1="0" y1="220" x2="525" y2="220" stroke="var(--accent-red)" stroke-width="2"/>
  </svg>

  <div class="name-tab">
    <p class="person-name"><strong>Dorian</strong> Walsh</p>
    <p class="person-role">Manager</p>
  </div>

  <div class="front-brand">
    <h1 class="brand-name">Corvello</h1>
    <p class="brand-tagline">Wheel Works</p>
  </div>

  <p class="front-address">48362 1/2 Parkfield rd, Brenford NV 89931</p>

  <div class="contact-band">
    <p class="contact-item">
      <svg viewBox="0 0 12 12"><path d="M2.5 0.5l2 2.2-1 1.3c0.6 1.6 2 3 3.5 3.5l1.3-1 2.2 2-1 2.5C5.5 11 1 6.5 0.5 1.5z"/></svg>
      555-214-7730
    </p>
    <p class="contact-item">
      <svg viewBox="0 0 12 12"><rect x="0.5" y="2" width="11" height="8" rx="1"/><polygon points="1,2.5 6,6.5 11,2.5" fill="var(--band-black)"/></svg>
      Dorian@corvellowheelandgarage.example
    </p>
    <p class="contact-item">
      <svg viewBox="0 0 12 12"><rect x="1" y="0.5" width="10" height="11" rx="1"/><rect x="3" y="2" width="6" height="3" fill="var(--band-black)"/></svg>
      555-214-7781
    </p>
    <p class="contact-item">
      <svg viewBox="0 0 12 12"><circle cx="6" cy="6" r="5.5"/><circle cx="6" cy="6" r="2.5" fill="var(--band-black)"/></svg>
      Corvellowheelandgarage.example
    </p>
  </div>
</section>

<section class="card card-back" aria-label="Business card back">
  <svg class="card-shapes" viewBox="0 0 525 300" preserveAspectRatio="none" aria-hidden="true">
    <polygon points="86,196 525,196 525,300 44,300" fill="var(--accent-red)"/>
    <polyline points="44,300 86,196 525,196" fill="none" stroke="var(--light-text)" stroke-width="3"/>
  </svg>

  <ul class="service-list">
    <li>New &amp; Used Tires</li>
    <li>Custom Wheels</li>
    <li>Lift Kits</li>
    <li>Shocks</li>
    <li>Brakes</li>
  </ul>

  <div class="back-brand">
    <h2 class="brand-name">Corvello</h2>
    <p class="brand-tagline">Wheel Works</p>
  </div>

  <div class="range-band">
    <p class="range-title">We carry the industry's finest</p>
    <p class="range-list">Ardent Forge · Alder Racing · KTV · RWL · ZEN · Halvor<br>QR Series · Ember · Rova Metal · Tessa · Kinto<br>Marlowe · Brightgate and many more</p>
  </div>
</section>

</body>
</html>
```